Designs for a Barrister's chambers

Design stationery (including business card and letterhead) for a barrister's chambers -- similar to a law firm, using the enclosed logo. The current designs are not fit for purpose.

```html
<!DOCTYPE html>
<html lang="en">
<head>
<meta charset="utf-8">
<title>Ledgerstone Chambers – Stationery</title>
<link rel="stylesheet" href="https://fonts.googleapis.com/css2?family=Red+Hat+Display:wght@500;700&family=Open+Sans:wght@400;600&family=Roboto:wght@400;500&display=swap">
<style>
  :root {
    --navy: #172a40;
    --navy-deep: #12233a;
    --teal: #1a8fa8;
    --teal-faint: #dde9ec;
    --paper: #f6f6f6;
    --ground: #e9e9e9;
    --ink: #4a4f55;
    --ink-dark: #2a2f35;
  }
  * { margin: 0; padding: 0; box-sizing: border-box; }
  html, body { width: 1200px; height: 795px; overflow: hidden; background: var(--ground); }
  .canvas { position: relative; width: 1200px; height: 795px; font-family: "Open Sans", sans-serif; color: var(--ink); }
  .sheet { position: absolute; background: var(--paper); overflow: hidden; }

  .brand-name { font-family: "Red Hat Display", sans-serif; font-weight: 700; color: var(--navy); line-height: 0.95; letter-spacing: -0.01em; }
  .brand { display: flex; align-items: center; }
  .brand-square { background: var(--teal); flex: none; }

  /* Letterhead */
  .letterhead { left: 293px; top: 99px; width: 293px; height: 415px; }
  .letterhead .brand { position: absolute; left: 28px; top: 33px; gap: 4px; }
  .letterhead .brand-square { width: 20px; height: 20px; }
  .letterhead .brand-name { font-size: 12px; }
  .contact-block { position: absolute; left: 180px; top: 25px; font-family: "Roboto", sans-serif; font-size: 4.6px; line-height: 6.6px; color: var(--ink-dark); }
  .contact-block .ico { display: inline-block; width: 3.4px; height: 3.4px; border-radius: 1px; background: var(--teal); margin-right: 2px; vertical-align: -0.3px; }
  .letter-body { position: absolute; left: 25px; top: 104px; width: 242px; font-size: 5.3px; line-height: 8px; text-align: justify; }
  .letter-body p { margin-bottom: 8px; }
  .signature { width: 36px; height: 32px; background: #ececec; margin-top: 4px; }
  .letter-footer { position: absolute; left: 0; right: 0; top: 383px; text-align: center; font-family: "Roboto", sans-serif; font-size: 4.7px; line-height: 6.6px; color: var(--ink-dark); }

  /* Folder */
  .folder { left: 637px; top: 80px; width: 346px; height: 436px; background: var(--navy); }
  .folder-spine { position: absolute; left: 0; top: 0; width: 18px; height: 100%; background: var(--navy-deep); border-right: 1px solid #1e3450; }
  .folder .brand { position: absolute; left: 18px; right: 0; top: 180px; flex-direction: column; gap: 14px; }
  .folder .brand-square { width: 36px; height: 36px; }
  .folder .brand-name { font-size: 26px; color: var(--teal); text-align: center; }
  .folder-url { position: absolute; left: 18px; right: 0; top: 401px; text-align: center; font-family: "Roboto", sans-serif; font-size: 9px; color: #e5edf2; letter-spacing: 0.02em; }
  .folder-url span { color: var(--teal); }

  /* Business cards */
  .card-front { left: 187px; top: 551px; width: 132px; height: 74px; background: var(--navy); }
  .card-front .brand-name { position: absolute; left: 10px; top: 50px; font-size: 8px; color: #f2f5f7; }
  .card-front .brand-square { position: absolute; left: 78px; top: 11px; width: 54px; height: 63px; }
  .card-back { left: 187px; top: 646px; width: 132px; height: 75px; }
  .holder-name { position: absolute; left: 9px; top: 13px; font-family: "Roboto", sans-serif; font-weight: 500; font-size: 4.4px; color: var(--ink-dark); }
  .holder-role { position: absolute; left: 9px; top: 18px; font-family: "Roboto", sans-serif; font-size: 3.6px; color: var(--teal); }
  .card-back .brand { position: absolute; left: 69px; top: 10px; gap: 3px; }
  .card-back .brand-square { width: 12px; height: 12px; }
  .card-back .brand-name { font-size: 7.3px; }
  .card-contacts { position: absolute; left: 9px; top: 44px; font-family: "Roboto", sans-serif; font-size: 3.4px; line-height: 4.5px; color: var(--ink-dark); }
  .card-address { position: absolute; right: 9px; top: 57px; text-align: right; font-family: "Roboto", sans-serif; font-size: 3.4px; line-height: 4.5px; color: var(--ink-dark); }

  /* Envelope front */
  .envelope-front { left: 353px; top: 561px; width: 329px; height: 157px; }
  .envelope-front .brand { position: absolute; left: 21px; top: 21px; gap: 4px; }
  .envelope-front .brand-square { width: 21px; height: 21px; }
  .envelope-front .brand-name { font-size: 12px; }
  .envelope-address { position: absolute; left: 21px; top: 46px; width: 112px; text-align: center; font-family: "Roboto", sans-serif; font-size: 6px; line-height: 7.4px; color: var(--ink-dark); }
  .envelope-accent { position: absolute; left: 197px; top: 20px; width: 132px; height: 137px; background: var(--teal-faint); opacity: 0.6; }

  /* Envelope back */
  .envelope-back { left: 713px; top: 561px; width: 329px; height: 157px; }
  .envelope-flap { position: absolute; left: 0; top: 0; width: 329px; height: 50px; background: var(--navy); clip-path: polygon(0 0, 100% 0, 98% 100%, 2% 100%); }
  .envelope-flap .brand-square { position: absolute; left: 151px; top: 13px; width: 27px; height: 27px; }
  .envelope-seam { position: absolute; left: 6px; right: 6px; top: 54px; height: 1px; background: #e4e4e4; }
</style>
</head>
<body>
<div class="canvas">

  <section class="sheet letterhead">
    <div class="brand"><span class="brand-square"></span><div class="brand-name">Ledgerstone<br>Chambers</div></div>
    <div class="contact-block">
      Address : 48 Arden Row,<br>London&nbsp; EC2B 7LT<br>
      <span class="ico"></span>0201 555 0140<br>
      <span class="ico"></span>0201 555 0141<br>
      <span class="ico"></span>clerks@ledgerstonechambers.com<br>
      <span class="ico"></span>www.ledgerstonechambers.com
    </div>
    <div class="letter-body">
      <p>Dear customer,</p>
      <p>Lorem ipsum dolor sit amet, consectetur adipisicing elit, sed do eiusmod tempor incididunt ut labore et dolore magna aliqua. Ut enim ad minim veniam, quis nostrud exercitation ullamco laboris nisi ut aliquip ex ea commodo consequat. Duis aute irure dolor in reprehenderit in voluptate velit esse cillum dolore eu fugiat nulla pariatur. Excepteur sint occaecat cupidatat non proident, sunt in culpa qui officia deserunt mollit anim id est laborum.</p>
      <p>Lorem ipsum dolor sit amet, consectetur adipisicing elit, sed do eiusmod tempor incididunt ut labore et dolore magna aliqua. Ut enim ad minim veniam, quis nostrud exercitation ullamco laboris nisi ut aliquip ex ea commodo consequat. Duis aute irure dolor in reprehenderit in voluptate velit esse cillum dolore eu fugiat nulla pariatur. Excepteur sint occaecat cupidatat non proident, sunt in culpa qui officia deserunt mollit anim id est laborum.</p>
      <p>Lorem ipsum dolor sit amet, consectetur adipisicing elit, sed do eiusmod tempor incididunt ut labore et dolore magna aliqua. Ut enim ad minim veniam, quis nostrud exercitation ullamco laboris nisi ut aliquip ex ea commodo consequat. Duis aute irure dolor in reprehenderit in voluptate velit esse cillum dolore eu fugiat nulla pariatur. Excepteur sint occaecat cupidatat non proident, sunt in culpa qui officia deserunt mollit anim id est laborum.</p>
      <p>Lorem ipsum dolor sit amet, consectetur adipisicing elit, sed do eiusmod tempor incididunt ut labore et dolore magna aliqua. Ut enim ad minim veniam, quis nostrud exercitation ullamco laboris nisi ut aliquip ex ea commodo consequat. Duis aute irure dolor in reprehenderit.</p>
      <p>Yours Sincerely,</p>
      <div class="signature" role="img" aria-label="Handwritten signature"></div>
    </div>
    <div class="letter-footer">
      Ledgerstone Chambers Limited | Company Reg No: 10293847<br>
      Registered Address: 12 Quay Walk, Harbourside, London SE9 4RT VAT Registration No: 84720193
    </div>
  </section>

  <section class="sheet folder">
    <div class="folder-spine"></div>
    <div class="brand"><span class="brand-square"></span><div class="brand-name">Ledgerstone<br>Chambers</div></div>
    <div class="folder-url">www.<span>ledgerstonechambers</span>.com</div>
  </section>

  <section class="sheet card-front">
    <span class="brand-square"></span>
    <div class="brand-name">Ledgerstone<br>Chambers</div>
  </section>

  <section class="sheet card-back">
    <div class="holder-name">MARTIN HALE</div>
    <div class="holder-role">Barrister</div>
    <div class="brand"><span class="brand-square"></span><div class="brand-name">Ledgerstone<br>Chambers</div></div>
    <div class="card-contacts">
      07700 900 412<br>0201 555 0140<br>0201 555 0141<br>martin.hale@ledgerstonechambers.com<br>www.ledgerstonechambers.com
    </div>
    <div class="card-address">48 Arden Row,<br>London&nbsp; EC2B 7LT</div>
  </section>

  <section class="sheet envelope-front">
    <div class="envelope-accent"></div>
    <div class="brand"><span class="brand-square"></span><div class="brand-name">Ledgerstone<br>Chambers</div></div>
    <div class="envelope-address">Address : 48 Arden Row,<br>London&nbsp; EC2B 7LT</div>
  </section>

  <section class="sheet envelope-back">
    <div class="envelope-flap"><span class="brand-square"></span></div>
    <div class="envelope-seam"></div>
  </section>

</div>
</body>
</html>
```